Travolinex Web Design

We would like to have our website designed and coded. It will be a display only website - no input or output functionality. It's a fairly simple structure with not many pages, but we would like some professional design and creative elements added in to make the site attractive and sharp. I have attached a presentation with the page and content layout. Where images are included in the presentation, those are concepts that you can reorganize or layout in any way that you think looks best. Same with the wheel of services on the incubator page, and the bullet points listed on the accelerator page.

```html
<!DOCTYPE html>
<html lang="en">
<head>
<meta charset="utf-8">
<title>Travolinex</title>
<link href="https://fonts.googleapis.com/css2?family=Roboto:wght@300;400;500;700&display=swap" rel="stylesheet">
<style>
:root{
  --navy:#0d4468;
  --navy-deep:#0b3b5b;
  --hero-a:#2f5c7d;
  --hero-b:#1b4868;
  --ink:#1d2230;
  --body:#8a8a8a;
  --grey-bg:#f6f6f6;
  --card:#ffffff;
  --icon-bg:#e4edf6;
  --icon-line:#7d90a6;
  --white:#ffffff;
  --map-sea:#5fb4e6;
  --footer-muted:#2f6a92;
}
*{margin:0;padding:0;box-sizing:border-box}
html,body{width:1200px;height:3074px;overflow:hidden}
body{font-family:'Roboto',sans-serif;color:var(--ink);background:var(--white)}
.wrap{width:900px;margin:0 auto;position:relative}

.site-header{height:88px;background:var(--white)}
.site-header .wrap{display:flex;align-items:center;height:88px}
.brand{font-weight:700;font-size:22px;color:var(--navy);letter-spacing:1px}
.nav{margin-left:auto;display:flex;align-items:center;gap:37px;font-size:13px;color:#222}
.nav-cta{background:var(--navy);color:var(--white);padding:9px 20px;font-size:13px;margin-left:1px}

.hero{height:552px;background:linear-gradient(180deg,var(--hero-a),var(--hero-b));text-align:center;color:var(--white);position:relative}
.hero-name{padding-top:222px;font-size:74px;font-weight:500;letter-spacing:6px;line-height:1}
.hero-text{margin:30px auto 0;width:760px;font-size:17.5px;font-weight:300;line-height:34px}
.hero-btn{display:inline-block;margin-top:22px;background:var(--white);color:var(--navy);font-size:18px;width:153px;height:47px;line-height:47px}

.about{height:493px}
.about .wrap{display:flex;padding-top:80px}
.about-photo{width:455px;height:332px;background:linear-gradient(180deg,#8da2ad 0%,#5f8697 45%,#b9b4a8 75%,#8c8982 100%)}
.about-copy{margin-left:43px;width:402px}
.about-copy h2{font-size:44px;font-weight:500;margin-top:11px;margin-bottom:22px}
.about-copy p{font-size:13px;color:var(--body);line-height:26.4px;margin-bottom:22px}

.services{height:655px;background:var(--grey-bg);text-align:center}
.services h2{font-size:44px;font-weight:500;padding-top:40px}
.lead{font-size:13px;color:var(--body);line-height:26.4px;margin-top:28px}
.cards{display:grid;grid-template-columns:279px 279px 279px;column-gap:31px;row-gap:27px;justify-content:space-between;margin-top:47px;text-align:left}
.card{background:var(--card);height:125px;position:relative;display:flex;align-items:center;padding:0 28px 0 32px;font-size:16px;line-height:30px;color:var(--ink);box-shadow:0 2px 8px rgba(0,0,0,.04)}
.card:nth-child(3n+2){padding-left:29px}
.card:nth-child(3n){padding-left:26px}
.card-icon{position:absolute;right:0;bottom:0;width:58px;height:58px;background:var(--icon-bg)}
.card-icon svg{position:absolute;left:10px;top:10px}
.summary{margin-top:40px;font-size:14.5px;color:#222}

.world{height:982px;text-align:center}
.world h2{font-size:44px;font-weight:500;padding-top:78px}
.world .lead{margin-top:37px}
.world-map{width:900px;height:480px;margin-top:36px;background:linear-gradient(90deg,var(--map-sea),#7cc2ea 50%,var(--map-sea))}
.world .lead.after{margin-top:40px}
.world .lead.after+.lead{margin-top:28px}

.site-footer{height:392px;background:var(--navy);color:var(--white)}
.site-footer .wrap{display:flex;padding-top:50px;height:323px}
.footer-brand{width:355px}
.footer-brand .brand{color:var(--white);font-size:21px}
.footer-brand p{font-size:13px;line-height:34.6px;margin-top:11px}
.col{font-size:13px}
.col.links{width:188px}
.col.company{width:189px}
.col h3{font-size:16px;font-weight:500;letter-spacing:1px;margin-top:6px;margin-bottom:14px}
.col li{list-style:none;line-height:34.6px}
.col.contact li{display:flex;align-items:center;gap:8px}
.legal{border-top:1px solid #1a537a;text-align:center;font-size:13px;color:var(--footer-muted);padding-top:24px;height:69px}
</style>
</head>
<body>

<header class="site-header">
  <div class="wrap">
    <div class="brand">TRAVOLINEX</div>
    <nav class="nav">
      <span>Incubator</span><span>Accelerator</span><span>UAE Distribution</span><span>References</span>
      <span class="nav-cta">Contact Us</span>
    </nav>
  </div>
</header>

<section class="hero" role="img" aria-label="Dubai skyline photo with blue overlay">
  <div class="hero-name">TRAVOLINEX</div>
  <p class="hero-text">Travolinex is a global incubator for start-up and early-stage medical device companies and serves as a growth accelerator for more advancedmedical device companies.</p>
  <span class="hero-btn">Contact Us</span>
</section>

<section class="about">
  <div class="wrap">
    <div class="about-photo" role="img" aria-label="Historic photo of people on a beach with wooden boats in the water"></div>
    <div class="about-copy">
      <h2>About Us</h2>
      <p>Travolinex is a global incubator for start-up and early-stage medical device companies and serves as a growth accelerator for more advanced medical device companies.</p>
      <p>Located in Harbourline Tech Park, a fully integrated technology park with the aim to foster technology and entrepreneurship, Travolinex provides active operational support to medical device companies through the expertise of highly experienced and well-connected industry veterans.</p>
    </div>
  </div>
</section>

<section class="services">
  <div class="wrap">
    <h2>Lorem Ipsum</h2>
    <p class="lead">These veterans serve as mentors, interim-managers or as freelance consultants, enabling medical device companies to outsource key operational functions, lowering monthly operating expenses and minimizing operational risks. Along with the operational support Travolinex provides, we utilize our global network of strategic partners, distributors, manufacturers and healthcare providers to:</p>
    <div class="cards">
      <div class="card">Raise Capital
        <span class="card-icon"><svg width="48" height="48" fill="none" stroke="var(--icon-line)" stroke-width="3"><path d="M2 48V26h12v22M14 48V14h14v34M28 48V24h10v24M20 8v6M7 33h3M7 40h3M20 22h3M20 30h3"/></svg></span></div>
      <div class="card">Assist and drive M&amp;A strategies
        <span class="card-icon"><svg width="48" height="48" fill="none" stroke="var(--icon-line)" stroke-width="3"><path d="M4 48V30h8a5 5 0 0 0 0-10H4V12h14a5 5 0 0 1 10 0h14"/></svg></span></div>
      <div class="card">Develop global sales and marketing strategies
        <span class="card-icon"><svg width="48" height="48" fill="none" stroke="var(--icon-line)" stroke-width="3"><rect x="2" y="8" width="44" height="38" rx="4"/><path d="M9 16l8 8M17 16l-8 8M26 38l16-16"/><circle cx="13" cy="36" r="3"/></svg></span></div>
      <div class="card">Build and expand distribution channels
        <span class="card-icon"><svg width="48" height="48" fill="none" stroke="var(--icon-line)" stroke-width="3"><path d="M4 48V36h8v12M20 48V28h8v12M36 48V22h8v26M4 24L36 4M28 4h8v8"/></svg></span></div>
      <div class="card">Source suppliers and assist in outsourcing production
        <span class="card-icon"><svg width="48" height="48" fill="none" stroke="var(--icon-line)" stroke-width="3"><circle cx="24" cy="14" r="10"/><path d="M6 46c0-10 8-18 18-18s18 8 18 18"/></svg></span></div>
      <div class="card">Support in Regulatory Affairs
        <span class="card-icon"><svg width="48" height="48" fill="none" stroke="var(--icon-line)" stroke-width="3"><path d="M2 40l10-10 6 4 10-12 6 2 8-10M4 48c6-4 12-2 18-6s12-2 18-6"/></svg></span></div>
    </div>
    <p class="summary">Travolinex helps your business minimize operational risk, operate more cost-effective, grow faster and increase profitability.</p>
  </div>
</section>

<section class="world">
  <div class="wrap">
    <h2>Located in Dubai – Covering the world</h2>
    <p class="lead">The story of Dubai - from a small fishing village of palm frond huts to the most modern city in the world. In a matter of 20 years Dubai has shown the world what ambition, vision and leadership, coupled with determination to overcome the odds, can achieve.</p>
    <div class="world-map" role="img" aria-label="World map with route lines connecting Dubai to partner locations worldwide"></div>
    <p class="lead after">The story of Dubai symbolizes the ambition of many corporations and leaders around the globe. We are proud to call Dubai our home for the past 20 years, having witnessed the most dynamic phase of that growth.</p>
    <p class="lead">The Dubai story has inspired the founding of Travolinex. A globally connected company, driven by passionate medical device industry experts, aiming for the exceptional and never the average. Connecting the global medical device world, helping young and established medical device companies to accelerate. Always with the goal to become the best - as impossible as it might seem.</p>
  </div>
</section>

<footer class="site-footer">
  <div class="wrap">
    <div class="footer-brand">
      <div class="brand">TRAVOLINEX</div>
      <p>Travolinex is a global incubator for start-up<br>and early-stage medical device companies<br>and serves as a growth accelerator for more<br>advanced medical device companies.</p>
    </div>
    <div class="col links"><h3>Quick Links</h3><ul><li>Incubator</li><li>Accelerator</li><li>UAE Distribution</li><li>References</li></ul></div>
    <div class="col company"><h3>Company</h3><ul><li>Privacy Policy</li><li>T &amp; C</li><li>News</li><li>Contact Us</li></ul></div>
    <div class="col contact"><h3>Contact Us</h3><ul>
      <li><svg width="12" height="12" viewBox="0 0 24 24" fill="#fff"><path d="M6.6 10.8a15 15 0 0 0 6.6 6.6l2.2-2.2a1 1 0 0 1 1-.25 11 11 0 0 0 3.6.6 1 1 0 0 1 1 1V20a1 1 0 0 1-1 1A17 17 0 0 1 3 4a1 1 0 0 1 1-1h3.5a1 1 0 0 1 1 1 11 11 0 0 0 .6 3.6 1 1 0 0 1-.25 1z"/></svg>+44 200-5180-417</li>
      <li><svg width="12" height="10" viewBox="0 0 24 18" fill="#fff"><path d="M0 0h24v18H0z" fill="#fff"/><path d="M0 0l12 9 12-9" stroke="#0d4468" stroke-width="2" fill="none"/></svg>info@travolinex.com</li>
      <li><svg width="12" height="14" viewBox="0 0 24 30" fill="#fff"><path d="M12 0a11 11 0 0 0-11 11c0 8 11 19 11 19s11-11 11-19A11 11 0 0 0 12 0zm0 15a4 4 0 1 1 0-8 4 4 0 0 1 0 8z"/></svg>Lorem Ipsum</li>
      <li><svg width="12" height="14" viewBox="0 0 24 30" fill="#fff"><path d="M12 0a11 11 0 0 0-11 11c0 8 11 19 11 19s11-11 11-19A11 11 0 0 0 12 0zm0 15a4 4 0 1 1 0-8 4 4 0 0 1 0 8z"/></svg>Lorem Ipsum dolor sit</li>
    </ul></div>
  </div>
  <div class="legal">Copyright © Travolinex 2021 . All rights reserved</div>
</footer>

</body>
</html>
```